Brookvane Holdings Ltd - Logo and Business Card

Create a logo and business card design for our new company.

Canadian private investment company with holdings in Saskatchewan Oil and real-estate.

Target Market(s)

Investors

Industry/Entity Type

Finance

Contact Information for Business Card

Logo
Name - Dalton Pryce
Position - President
Phone - 306.482.7159
Website - www.brookvaneholdings.ca

Logo Text

Today. Tomorrow. Together. (Tag Line)

Colors

Designer to choose colors to be used in the design.

Requirements
Must have
• Logo Must Have - Type Font only
• Must be modern, professional and stand out from the crowd.
Nice to have
• Don't have any, blank slate.

```html
<!DOCTYPE html>
<html lang="en">
<head>
<meta charset="utf-8">
<title>Brookvane Holdings Ltd – Business Card</title>
<link href="https://fonts.googleapis.com/css2?family=Open+Sans:wght@300;400;700&display=swap" rel="stylesheet">
<style>
  :root {
    --backdrop: #e6e6e4;
    --paper: #ffffff;
    --navy: #16284a;
    --ink: #7a7c80;
    --ink-dark: #4a4c50;
    --on-navy: #ffffff;
  }
  * { margin: 0; padding: 0; box-sizing: border-box; }
  html, body {
    width: 1200px; height: 1021px; overflow: hidden;
    background: var(--backdrop);
    font-family: "Open Sans", Arial, sans-serif;
  }
  .canvas { position: relative; width: 1200px; height: 1021px; }

  .card {
    position: absolute;
    width: 520px; height: 297px;
    box-shadow: 0 10px 24px rgba(0,0,0,.18);
  }
  .card--front { left: 110px; top: 150px; background: var(--paper); }
  .card--back  { left: 570px; top: 470px; background: var(--navy); }

  /* Wordmark: one colour, one weight, two lines */
  .wordmark {
    font-weight: 300;
    text-transform: uppercase;
    white-space: nowrap;
    line-height: 1;
  }
  .wordmark__main { display: block; letter-spacing: 1px; }
  .wordmark__sub  { display: block; margin-top: .35em; }

  .card--front .wordmark {
    position: absolute; left: 40px; top: 140px;
    color: var(--navy);
  }
  .card--front .wordmark__main { font-size: 26px; }
  .card--front .wordmark__sub  { font-size: 9px; letter-spacing: 5.6px; }

  .card--back .wordmark {
    position: absolute; left: 0; right: 0; top: 118px;
    text-align: center; color: var(--on-navy);
  }
  .card--back .wordmark__main { font-size: 34px; }
  .card--back .wordmark__sub  { font-size: 11px; letter-spacing: 7.6px; }

  .contact { position: absolute; left: 292px; top: 72px; }
  .contact__name { font-size: 21px; font-weight: 300; color: var(--ink); line-height: 1.1; }
  .contact__name strong { font-weight: 700; color: var(--ink-dark); }
  .contact__role { font-size: 12px; font-weight: 700; color: var(--navy); margin-bottom: 14px; }
  .contact__list { list-style: none; }
  .contact__item {
    display: flex; align-items: center; gap: 10px;
    font-size: 11px; color: var(--ink); margin-bottom: 9px;
  }
  .contact__item svg { width: 13px; height: 13px; fill: var(--navy); flex: none; }

  .signature-logo {
    position: absolute; left: 60px; top: 880px;
    color: var(--navy);
  }
  .signature-logo .wordmark__main { font-size: 62px; }
  .signature-logo .wordmark__sub  { font-size: 17px; letter-spacing: 12.5px; margin-top: .45em; }
</style>
</head>
<body>
<main class="canvas">
  <section class="card card--front">
    <div class="wordmark">
      <span class="wordmark__main">Brookvane</span>
      <span class="wordmark__sub">Holdings Ltd</span>
    </div>
    <div class="contact">
      <p class="contact__name">Dalton <strong>Pryce</strong></p>
      <p class="contact__role">President</p>
      <ul class="contact__list">
        <li class="contact__item">
          <svg viewBox="0 0 16 16" aria-hidden="true"><path d="M2 5c0-2 2-3 6-3s6 1 6 3v1h-3V5H5v1H2zM4 7h8l2 6H2z"/><circle cx="8" cy="10" r="1.5" fill="#fff"/></svg>
          306.482.7159
        </li>
        <li class="contact__item">
          <svg viewBox="0 0 16 16" aria-hidden="true"><path d="M1 3h14v10H1zM2 4l6 5 6-5" fill="none" stroke="#16284a" stroke-width="1.4"/></svg>
          dalton@brookvaneholdings.ca
        </li>
        <li class="contact__item">
          <svg viewBox="0 0 16 16" aria-hidden="true"><g fill="none" stroke="#16284a" stroke-width="1.2"><circle cx="8" cy="8" r="6.5"/><ellipse cx="8" cy="8" rx="2.8" ry="6.5"/><path d="M1.5 8h13"/></g></svg>
          www.brookvaneholdings.ca
        </li>
      </ul>
    </div>
  </section>

  <section class="card card--back">
    <div class="wordmark">
      <span class="wordmark__main">Brookvane</span>
      <span class="wordmark__sub">Holdings Ltd</span>
    </div>
  </section>

  <div class="wordmark signature-logo">
    <span class="wordmark__main">Brookvane</span>
    <span class="wordmark__sub">Holdings Ltd</span>
  </div>
</main>
</body>
</html>
```